Stationery Design Project - Professional Training Company

Full set of statinery in PDF and format that can be given to the printers

Letterhead
Business cards x 3
Compliments slip
Envelope
Updates

Many thanks for all your contributions, the quality of the designs is amazing.

Thank you all so much for your contribution to this project, I am very impressed with the designs and choice of designs, you are all clearly very talented individuals.

I hope to be making a decision on the final choice this evening UAE time.

Best regards and again thank you so much

Desmond

I would like to take this opportunity to thank you all for your contributions, I have been very impressed with each of the designs submitted.

I will shortly go back and give each of you a personal rating on each of your designs.

Again thank you all so much for your efforts

Best Regards

Desmond

Target Market(s)

We are a training company that provides IT training for Medical and Professional Staff, we train professional adults

Industry/Entity Type

Business

Requirements
Must have
• The letterhead and compliments slip must have at the bottom of the page:-

Bright Harbor Learning LLP operates as a limited liability partnership registered in England and Wales (with registered number OC742168)

Business Cards are to be made up for three people (details of those to be provided after appoval of design but are included in this project) and should contain:

Name
Title
Telephone
email
Address: P.O. Box 518243 Dubai UAE
web address: www.brightharborlearning.example
Nice to have
• Very clean and professional looking
Should not have
• No look to busy or ovr crowded

```html
<!DOCTYPE html>
<html lang="en">
<head>
<meta charset="utf-8">
<title>Bright Harbor Learning LLP – Business Card</title>
<link href="https://fonts.googleapis.com/css2?family=Open+Sans:wght@400;600;700&display=swap" rel="stylesheet">
<style>
  :root {
    --backdrop: #dcdcdc;
    --card: #f7f7f5;
    --ink: #2b2b2b;
    --plum: #6e1a63;
    --plum-dark: #3a1438;
    --leaf: #3d8a1f;
    --rule: #9a9a9a;
  }
  * { margin: 0; padding: 0; box-sizing: border-box; }
  html, body {
    width: 1200px; height: 900px; overflow: hidden;
    background: var(--backdrop);
    font-family: "Open Sans", Arial, sans-serif;
    color: var(--ink);
  }
  .sheet {
    position: relative; width: 1200px; height: 900px;
    display: flex; flex-direction: column; align-items: center; justify-content: center; gap: 60px;
  }
  .card {
    position: relative; width: 600px; height: 343px;
    background: var(--card);
    box-shadow: 0 4px 14px rgba(0,0,0,0.18);
    overflow: hidden;
  }
  .brand {
    display: flex; align-items: center; gap: 12px;
    color: var(--plum-dark); font-weight: 600; letter-spacing: -0.3px;
  }
  .brand-mark { width: 34px; height: 34px; background: var(--plum); flex: none; }
  .brand-name { font-size: 22px; line-height: 1.1; }

  /* front */
  .card-front { display: flex; flex-direction: column; align-items: center; justify-content: center; }
  .card-front .brand { margin-top: -10px; }
  .card-front .web {
    position: absolute; bottom: 74px; left: 0; right: 0; text-align: center;
    font-size: 12px; letter-spacing: 1.6px; color: var(--ink);
  }

  /* back */
  .card-back .brand { position: absolute; left: 34px; top: 72px; }
  .holder { position: absolute; right: 40px; top: 68px; text-align: right; }
  .holder-name { color: var(--plum); font-weight: 700; font-size: 17px; }
  .holder-title { font-size: 12px; }
  .divider { position: absolute; left: 34px; right: 0; top: 196px; border-top: 1px solid var(--rule); }
  .contacts { position: absolute; left: 34px; top: 208px; list-style: none; font-size: 14px; line-height: 21px; }
  .contacts li { display: flex; align-items: center; gap: 10px; }
  .contacts svg { width: 13px; height: 13px; fill: var(--plum-dark); flex: none; }
  .address { position: absolute; right: 40px; top: 220px; text-align: right; font-size: 12.5px; line-height: 17px; }
  .band { position: absolute; left: 0; right: 0; bottom: 0; height: 14px; display: flex; }
  .band-leaf { flex: 0 0 73%; background: var(--leaf); }
  .band-plum { flex: 1; background: var(--plum); margin-left: 3px; }
</style>
</head>
<body>
<main class="sheet">
  <section class="card card-front" aria-label="Business card front">
    <div class="brand">
      <span class="brand-mark"></span>
      <span class="brand-name">Bright Harbor Learning LLP</span>
    </div>
    <p class="web">www.brightharborlearning.example</p>
  </section>

  <section class="card card-back" aria-label="Business card back">
    <div class="brand">
      <span class="brand-mark"></span>
      <span class="brand-name">Bright Harbor Learning LLP</span>
    </div>
    <div class="holder">
      <p class="holder-name">Karim Haddad</p>
      <p class="holder-title">President</p>
    </div>
    <div class="divider"></div>
    <ul class="contacts">
      <li><svg viewBox="0 0 16 16" aria-hidden="true"><path d="M3 1h3l1.5 4-2 1.3a9 9 0 0 0 4.2 4.2L11 8.5l4 1.5v3a2 2 0 0 1-2 2A12 12 0 0 1 1 3a2 2 0 0 1 2-2z"/></svg>+971(2)4615302</li>
      <li><svg viewBox="0 0 16 16" aria-hidden="true"><path d="M4 1h8v4H4zM1 6h14v6h-3v3H4v-3H1zm4 4v3h6v-3z"/></svg>+971(2)4615303</li>
      <li><svg viewBox="0 0 16 16" aria-hidden="true"><path d="M8 1a7 7 0 1 0 3.5 13l-.7-1.3A5.5 5.5 0 1 1 13.5 8v.8a1.2 1.2 0 0 1-2.4 0V4.5H9.7v.6A3.3 3.3 0 1 0 10 11a2.6 2.6 0 0 0 5-2.2V8A7 7 0 0 0 8 1zm0 5a2 2 0 1 1 0 4 2 2 0 0 1 0-4z"/></svg>karim@brightharborlearning.example</li>
      <li><svg viewBox="0 0 16 16" aria-hidden="true"><path d="M8 1a7 7 0 1 0 0 14A7 7 0 0 0 8 1zm-5.4 6h2.5a11 11 0 0 1 .6-3.6A5.5 5.5 0 0 0 2.6 7zm0 2a5.5 5.5 0 0 0 3.1 3.6A11 11 0 0 1 5.1 9zm4 0c.1 2 .7 3.6 1.4 4.4.7-.8 1.3-2.4 1.4-4.4zm0-2h2.8C9.3 5 8.7 3.4 8 2.6 7.3 3.4 6.7 5 6.6 7zm4.3 2a11 11 0 0 1-.6 3.6A5.5 5.5 0 0 0 13.4 9zm2.5-2a5.5 5.5 0 0 0-3.1-3.6c.3 1 .6 2.3.6 3.6z"/></svg>www.brightharborlearning.example</li>
    </ul>
    <address class="address" style="font-style:normal">
      P.O. Box 518243 Dubai<br>United Arab Emirates
    </address>
    <div class="band"><span class="band-leaf"></span><span class="band-plum"></span></div>
  </section>
</main>
</body>
</html>
```